Tolvern Business Cards

Business card design. dont mind if new logo is suggested.
it would be for a security company.
our clients would be bigger security companies around Australia.
have a logo done but can be replaced. see attaached. like the colors.
Need company name, person name, designation, phone and email on front.
At back company logo and name. website saddress and 2 x license numbers
would like to have 2 different background color for both sidde

Industry/Entity Type

Security

Contact Information for Business Card

round corners, front should be light in color. need logo at back with webaddress and 2 x license numners

Font styles to use
Sans Serif

Colors
f37122
faa54b
f8ba93
0255a3
0592cd
85cae6
b3d448
9bcb3c
ffffff

Requirements
Must have
• see description
Nice to have
• see description
Should not have
• should not be difficult to read or hardd to find information on card.. lets say easy on eyes yet catchy

```html
<!DOCTYPE html>
<html lang="en">
<head>
<meta charset="utf-8">
<title>Tolvern Security Group – Business Cards</title>
<link rel="stylesheet" href="https://fonts.googleapis.com/css2?family=Alegreya+Sans+SC:wght@500;700&family=Lato:wght@400&display=swap">
<style>
  :root {
    --stage: #3a3b3d;
    --card-light: #fbfcfd;
    --tint-soft: #e6eef4;
    --navy: #0b2d63;
    --blue-deep: #06306e;
    --blue-mid: #0b55b0;
    --cyan: #1a9dc6;
    --ink: #1b3a6b;
    --white: #ffffff;
  }
  * { box-sizing: border-box; margin: 0; padding: 0; }
  html, body { width: 1200px; height: 900px; overflow: hidden; }
  body {
    background: var(--stage);
    display: flex;
    align-items: center;
    justify-content: center;
    gap: 60px;
  }
  .card {
    position: relative;
    width: 510px;
    height: 300px;
    border-radius: 24px;
    overflow: hidden;
  }
  /* Front */
  .card--front { background: var(--card-light); }
  .front-texture {
    position: absolute; inset: 0;
    background: radial-gradient(ellipse at 30% 60%, var(--tint-soft) 0%, var(--card-light) 75%);
  }
  .front-brand {
    position: absolute;
    left: 24px; top: 146px;
    display: flex; flex-direction: column; align-items: center; gap: 14px;
    width: 240px;
  }
  .brand-dot {
    width: 52px; height: 52px; border-radius: 50%;
    background: var(--cyan);
  }
  .brand-name {
    font-family: "Alegreya Sans SC", sans-serif;
    font-weight: 700;
    font-size: 21px;
    letter-spacing: 0.3px;
    color: var(--navy);
    white-space: nowrap;
  }
  .front-divider {
    position: absolute;
    left: 276px; top: 64px;
    width: 1px; height: 108px;
    background: var(--cyan);
  }
  .contact-block {
    position: absolute;
    left: 292px; top: 60px;
  }
  .person-name {
    font-family: "Alegreya Sans SC", sans-serif;
    font-weight: 700;
    font-size: 23px;
    color: var(--cyan);
    line-height: 1;
  }
  .person-role {
    font-family: "Alegreya Sans SC", sans-serif;
    font-weight: 500;
    font-size: 15px;
    color: var(--ink);
    margin-top: 4px;
    margin-bottom: 12px;
  }
  .contact-list { list-style: none; }
  .contact-item {
    display: flex; align-items: center; gap: 10px;
    font-family: "Lato", sans-serif;
    font-size: 14px;
    color: var(--ink);
    margin-bottom: 6px;
  }
  .contact-icon {
    width: 17px; height: 17px; border-radius: 50%;
    background: var(--cyan);
    display: flex; align-items: center; justify-content: center;
    flex: none;
  }
  /* Back */
  .card--back {
    background: radial-gradient(ellipse at 50% 38%, var(--blue-mid) 0%, var(--blue-deep) 70%);
    display: flex; flex-direction: column; align-items: center;
    padding-top: 48px;
    color: var(--white);
  }
  .card--back .brand-dot { background: var(--white); width: 58px; height: 58px; margin-bottom: 20px; }
  .card--back .brand-name { color: var(--white); font-size: 23px; }
  .licence-list { list-style: none; margin-top: 10px; text-align: center; }
  .licence {
    font-family: "Alegreya Sans SC", sans-serif;
    font-weight: 500;
    font-size: 15px;
    letter-spacing: 0.5px;
    line-height: 1.45;
  }
  .web {
    font-family: "Alegreya Sans SC", sans-serif;
    font-weight: 700;
    font-size: 15px;
    letter-spacing: 0.5px;
    margin-top: 20px;
  }
</style>
</head>
<body>
  <section class="card card--front">
    <div class="front-texture" role="img" aria-label="Soft pale bubble pattern background"></div>
    <div class="front-brand">
      <span class="brand-dot"></span>
      <span class="brand-name">Tolvern Security Group</span>
    </div>
    <div class="front-divider"></div>
    <div class="contact-block">
      <p class="person-name">Daniel Harker</p>
      <p class="person-role">Director</p>
      <ul class="contact-list">
        <li class="contact-item">
          <span class="contact-icon">
            <svg width="10" height="10" viewBox="0 0 10 10"><path d="M2 1 L4 1 L4.6 3 L3.4 3.8 Q4.3 5.7 6.2 6.6 L7 5.4 L9 6 L9 8 Q5 9 1 3 Z" fill="#fff"/></svg>
          </span>
          555-014-2288
        </li>
        <li class="contact-item">
          <span class="contact-icon">
            <svg width="10" height="8" viewBox="0 0 10 8"><rect x="0.5" y="0.5" width="9" height="7" fill="none" stroke="#fff"/><path d="M0.5 0.5 L5 4.5 L9.5 0.5" fill="none" stroke="#fff"/></svg>
          </span>
          info@tolverngroup.com
        </li>
        <li class="contact-item">
          <span class="contact-icon">
            <svg width="10" height="10" viewBox="0 0 10 10"><circle cx="5" cy="5" r="4" fill="none" stroke="#fff"/><path d="M1 5 H9 M5 1 Q2.5 5 5 9 M5 1 Q7.5 5 5 9" fill="none" stroke="#fff" stroke-width="0.8"/></svg>
          </span>
          www.tolverngroup.com
        </li>
      </ul>
    </div>
  </section>

  <section class="card card--back">
    <span class="brand-dot"></span>
    <span class="brand-name">Tolvern Security Group</span>
    <ul class="licence-list">
      <li class="licence">Licence No. 3061827</li>
      <li class="licence">Licence No. 4172906</li>
    </ul>
    <p class="web">www.tolverngroup.com</p>
  </section>
</body>
</html>
```